Qorby Labs

I am a CBD Manufacturer I would have a site more laid out in a lab format
current site is qorbylabs.example what Id like is a site like tarnwellabs.example

Target Market(s)

Any one needing cbd oil and finished goods

Coding

Coded - Design and coding required

Number of Pages Required

1 page

```html
<!DOCTYPE html>
<html lang="en">
<head>
<meta charset="utf-8">
<title>Qorby Labs – Full Spectrum CBD</title>
<link href="https://fonts.googleapis.com/css2?family=Poppins:wght@600;700;800&family=Montserrat:wght@400;500;600;700&display=swap" rel="stylesheet">
<style>
:root{
  --gold:#b8862c;
  --gold-light:#d9b43a;
  --cream:#fdf8ec;
  --ink:#1d1d1d;
  --text:#333;
  --grey-rule:#a9a9a9;
  --product-bg:#f4f0ee;
  --band:#f7eba0;
  --footer:#231f20;
  --footer-text:#e8e8e8;
  --white:#fff;
}
*{box-sizing:border-box;margin:0;padding:0}
html,body{width:1200px;height:3635px;overflow:hidden}
body{position:relative;font-family:"Montserrat",sans-serif;color:var(--text);background:var(--white)}
.abs{position:absolute}
h1,h2,h3{font-family:"Poppins",sans-serif;color:var(--ink)}
.rule{width:46px;height:3px;background:var(--grey-rule)}
.btn{position:absolute;background:var(--gold);color:var(--white);font-family:"Poppins",sans-serif;font-weight:700;display:flex;align-items:center;justify-content:center;letter-spacing:.3px}

/* header + hero */
.hero{left:0;top:0;width:1200px;height:664px;background:var(--cream)}
.brand{left:131px;top:34px;font-family:"Montserrat",sans-serif;font-weight:500;font-size:44px;color:var(--gold-light);letter-spacing:1px}
.mail{left:716px;top:20px;display:flex;align-items:center;gap:10px;white-space:nowrap}
.mail svg{flex:none}
.mail .sep{width:1px;height:32px;background:var(--gold);flex:none}
.mail small{display:block;font-size:11px;color:#444}
.mail span{font-size:13px;color:#222}
.login{left:930px;top:23px;width:71px;height:29px;border:1.5px solid var(--gold);border-radius:6px;color:var(--gold);font-size:12px;font-weight:600;display:flex;align-items:center;justify-content:center}
.cart{left:1022px;top:22px}
.nav{left:562px;top:79px;display:flex;gap:38px;font-size:15px;font-weight:600;color:#222}
.nav .active{color:var(--gold);text-decoration:underline;text-underline-offset:5px}
.hero-photo{left:131px;top:190px;width:521px;height:410px;border-radius:8px;background:radial-gradient(ellipse at 50% 55%,#2d2a8a 0%,#1a1748 55%,#fdf8ec 78%)}
.hero-title{left:741px;top:244px;font-size:40px;font-weight:800;line-height:48px;color:var(--gold)}
.hero-sub{left:741px;top:360px;font-size:23px;line-height:31px;color:#333;width:320px}
.arrow{width:34px;height:34px;background:#222;display:flex;align-items:center;justify-content:center}

/* knowledge */
.section-title{left:0;width:1200px;text-align:center;font-size:21px;font-weight:700}
.feature{position:absolute;top:825px;width:290px;text-align:center}
.feature svg{display:block;margin:0 auto 20px}
.feature h3{font-size:17px;font-weight:700;margin-bottom:12px}
.feature p{font-size:13px;line-height:19px;color:#333}

/* welcome */
.welcome{left:0;top:1161px;width:1200px;height:463px;background:linear-gradient(100deg,#18202c 0%,#3b4757 45%,#1b1f25 100%)}
.welcome h2{position:absolute;left:0;top:96px;width:1200px;text-align:center;color:var(--white);font-size:30px;font-weight:700}
.welcome p{position:absolute;left:330px;top:159px;width:540px;text-align:center;color:#eee;font-size:17px;line-height:22.5px}

/* benefits */
.benefits-photo{left:599px;top:1624px;width:601px;height:545px;background:linear-gradient(120deg,#cfd6dd,#eef1f4 45%,#b9c3cc)}
.benefits h2{position:absolute;left:131px;top:1686px;font-size:22px;font-weight:700;line-height:32px}
.benefit{position:absolute;left:136px;width:360px;display:flex;gap:12px;font-size:12.5px;line-height:19px;color:#333}
.benefit svg{flex:none;margin-top:2px}
.benefit-line{position:absolute;left:136px;width:352px;height:1px;background:#bbb}

/* products */
.products{left:0;top:2169px;width:1200px;height:500px;background:var(--product-bg)}
.card{position:absolute;top:2304px;width:223px;height:317px;background:var(--white);text-align:center}
.card .shot{margin:22px auto 0;width:178px;height:178px;background:linear-gradient(#e9e6e3,#c9c4bf)}
.card h3{margin-top:20px;font-size:14px;font-weight:600}
.card .price{font-size:14px;margin-top:4px}
.card .add{margin:10px auto 0;width:86px;height:21px;background:var(--gold);color:var(--white);font-size:9.5px;font-weight:700;font-family:"Poppins",sans-serif;display:flex;align-items:center;justify-content:center}

/* subscribe */
.sub-photo{left:0;top:2669px;width:599px;height:471px;background:linear-gradient(135deg,#c8d0e0,#8e9a7a 45%,#d9c46a 80%,#e8e4dc)}
.sub-title{left:664px;top:2741px;font-size:22px;font-weight:700}
.field{position:absolute;left:667px;width:396px;height:49px;border:1px solid #555;font-size:12px;color:#333;padding:0 18px;display:flex;align-items:center}

/* trust band */
.band{left:0;top:3140px;width:1200px;height:157px;background:var(--band)}
.trust{position:absolute;top:3180px;display:flex;align-items:center;gap:18px;font-family:"Poppins",sans-serif;font-weight:600;font-size:16px;color:#222}
.trust .dot{width:70px;height:70px;border-radius:50%;background:var(--gold);display:flex;align-items:center;justify-content:center}

/* footer */
.footer{left:0;top:3297px;width:1200px;height:338px;background:var(--footer)}
.foot-brand{left:131px;top:3390px;font-size:46px;font-weight:500;color:var(--white)}
.foot-col{position:absolute;top:3346px;font-size:11.5px;color:var(--footer-text)}
.foot-col h4{font-family:"Poppins",sans-serif;font-size:13px;font-weight:600;letter-spacing:.5px;color:var(--white);margin-bottom:16px}
.menu-list li{list-style:none;line-height:20px}
.contact-item{display:flex;gap:14px;align-items:center;margin-bottom:18px;line-height:15px}
.ico{width:24px;height:24px;border-radius:50%;background:var(--white);display:flex;align-items:center;justify-content:center;flex:none}
.legal{left:131px;top:3588px;font-size:11.5px;color:var(--footer-text)}
.copyright{left:860px;top:3588px;font-size:11.5px;color:var(--footer-text)}
</style>
</head>
<body>

<!-- Header & hero -->
<section class="abs hero"></section>
<div class="abs brand">Qorby Labs</div>
<div class="abs mail">
  <svg width="16" height="12" viewBox="0 0 16 12"><rect width="16" height="12" rx="1" fill="#b8862c"/><path d="M0 1l8 6 8-6" stroke="#fdf8ec" stroke-width="1.5" fill="none"/></svg>
  <div class="sep"></div>
  <div><small>E mail us</small><span>info@qorbylabs.example</span></div>
</div>
<div class="abs login">LOGIN</div>
<svg class="abs cart" width="38" height="34" viewBox="0 0 38 34"><path d="M2 6h6l4 16h18l4-12H10" fill="none" stroke="#222" stroke-width="2"/><circle cx="14" cy="28" r="2.5" fill="#222"/><circle cx="28" cy="28" r="2.5" fill="#222"/><circle cx="31" cy="7" r="7" fill="#b8862c"/><text x="31" y="10.5" font-size="10" fill="#fff" text-anchor="middle" font-family="Montserrat">0</text></svg>
<nav class="abs nav"><span class="active">HOME</span><span>COMMUNITY</span><span>SHOP</span><span>WHOLESALE</span><span>CONTACT</span></nav>
<div class="abs hero-photo" role="img" aria-label="Group of blue glass dropper bottles of 1000mg full spectrum CBD oil in assorted flavours"></div>
<h1 class="abs hero-title">FULL SPECTRUM<br>CBD OIL</h1>
<p class="abs hero-sub">We are proud to serve our community.</p>
<div class="btn" style="left:745px;top:452px;width:139px;height:44px;font-size:15px">READ MORE</div>
<div class="abs arrow" style="left:0;top:346px"><svg width="10" height="14"><path d="M8 1L2 7l6 6" stroke="#fff" stroke-width="2" fill="none"/></svg></div>
<div class="abs arrow" style="left:1166px;top:346px"><svg width="10" height="14"><path d="M2 1l6 6-6 6" stroke="#fff" stroke-width="2" fill="none"/></svg></div>

<!-- Knowledge -->
<h2 class="abs section-title" style="top:722px">KNOWLEDGE IS POWER</h2>
<div class="abs rule" style="left:577px;top:766px"></div>

<div class="feature" style="left:127px">
  <svg width="86" height="86" viewBox="0 0 86 86"><rect x="22" y="14" width="34" height="12" rx="2" fill="none" stroke="#222" stroke-width="3"/><rect x="16" y="28" width="46" height="52" rx="4" fill="none" stroke="#222" stroke-width="3"/><rect x="19" y="52" width="40" height="25" fill="#b8862c"/><path d="M60 78l18-22-6 16 12-6z" fill="#222"/></svg>
  <h3>WHAT IS CBD?</h3>
  <p>Cannabidiol also known as CBD, is a phytocannabinoid found in agricultural hemp. Unlike its cousin tetrahydrocannabinol also known as THC, CBD is non-psychotoxic, which means it does not produce feelings of euphoria.</p>
</div>
<div class="feature" style="left:455px">
  <svg width="86" height="86" viewBox="0 0 86 86"><rect x="6" y="14" width="72" height="52" fill="none" stroke="#222" stroke-width="3"/><rect x="18" y="28" width="36" height="5" fill="#b8862c"/><rect x="18" y="40" width="26" height="5" fill="#b8862c"/><circle cx="68" cy="64" r="7" fill="none" stroke="#b8862c" stroke-width="3"/><path d="M68 71v9" stroke="#b8862c" stroke-width="3"/></svg>
  <h3>IS IT LEGAL?</h3>
  <p>Because all of our CBD products are derived from agricultural hemp and compliant, it is not unlawful to ship across the United States.</p>
</div>
<div class="feature" style="left:787px">
  <svg width="86" height="86" viewBox="0 0 86 86"><path d="M43 6l20 8v16c0 12-9 20-20 24-11-4-20-12-20-24V14z" fill="#b8862c"/><path d="M34 30l7 7 12-12" stroke="#fff" stroke-width="4" fill="none"/><path d="M8 44l10 22 16 12 4-10-14-14z M78 44l-10 22-16 12-4-10 14-14z" fill="#222"/></svg>
  <h3>IS IT SAFE?</h3>
  <p>CBD has a remarkable safety profile and Qorby Labs goes beyond to ensure high quality, safety, and efficacy of our CBD products. All Qorby Labs products are derived from agricultural hemp, are non-psychotoxic, and are produced with care.</p>
</div>

<!-- Welcome -->
<section class="abs welcome" role="img" aria-label="Laboratory scene with a scientist working at a microscope, darkened">
  <h2>WELCOME TO QORBYLABS</h2>
  <p>Lorem ipsum dolor sit amet consectetur adipiscing elit sed do eiusmod tempor incididunt ut labore et dolore magna aliqua. Ut enim ad minim veniam, quis nostrud exercitation ullamco laboris nisi ut aliquip ex ea commodo consequat. Duis aute irure dolor in reprehenderit in voluptate velit esse.</p>
</section>
<div class="btn" style="left:532px;top:1470px;width:135px;height:42px;font-size:14px">READ MORE</div>

<!-- Benefits -->
<section class="benefits">
  <h2>DISCOVER THE BENEFITS OF<br>QORBY LABS CBD</h2>
  <div class="abs rule" style="left:131px;top:1760px"></div>
  <div class="benefit" style="top:1792px"><svg width="14" height="14" viewBox="0 0 14 14"><path d="M2 7l3 3 7-7" stroke="#b8862c" stroke-width="2.2" fill="none"/></svg><span>All of our products are tested to ensure the best quality CBD available</span></div>
  <div class="benefit-line" style="top:1845px"></div>
  <div class="benefit" style="top:1861px"><svg width="14" height="14" viewBox="0 0 14 14"><path d="M2 7l3 3 7-7" stroke="#b8862c" stroke-width="2.2" fill="none"/></svg><span>Choose from a wide variety of products and flavors including concentrate, edible, tincture, vape pen, body cream, salve, and ointment</span></div>
  <div class="benefit-line" style="top:1933px"></div>
  <div class="benefit" style="top:1950px"><svg width="14" height="14" viewBox="0 0 14 14"><path d="M2 7l3 3 7-7" stroke="#b8862c" stroke-width="2.2" fill="none"/></svg><span>We use CO2 extraction and a chemical-free extraction process that is environmentally friendly and safe for all of our hemp CBD oil</span></div>
  <div class="btn" style="left:136px;top:2045px;width:114px;height:35px;font-size:12px">READ MORE</div>
</section>
<div class="abs benefits-photo" role="img" aria-label="Scientist in lab coat and safety glasses working at laboratory equipment"></div>

<!-- Products -->
<section class="abs products"></section>
<h2 class="abs section-title" style="top:2214px">PRODUCTS</h2>
<div class="abs rule" style="left:577px;top:2259px"></div>
<svg class="abs" style="left:58px;top:2434px" width="14" height="26"><path d="M12 2L2 13l10 11" stroke="#aaa" stroke-width="2" fill="none"/></svg>
<svg class="abs" style="left:1110px;top:2434px" width="14" height="26"><path d="M2 2l10 11-10 11" stroke="#aaa" stroke-width="2" fill="none"/></svg>
<div class="card" style="left:127px"><div class="shot" role="img" aria-label="Boxed CBD vape pen cartridge"></div><h3>VAPE PEN</h3><div class="price">$35.00</div><div class="add">ADD TO CART</div></div>
<div class="card" style="left:367px"><div class="shot" role="img" aria-label="Round tin of CBD salve"></div><h3>SALVE</h3><div class="price">$120.00</div><div class="add">ADD TO CART</div></div>
<div class="card" style="left:606px"><div class="shot" role="img" aria-label="Roll-on CBD ointment bottle"></div><h3>ROLL ON OINTMENT</h3><div class="price">$99.00</div><div class="add">ADD TO CART</div></div>
<div class="card" style="left:846px"><div class="shot" role="img" aria-label="Black tube of CBD lotion"></div><h3>LOTION</h3><div class="price">$36.00</div><div class="add">ADD TO CART</div></div>

<!-- Subscribe -->
<div class="abs sub-photo" role="img" aria-label="Gloved hand holding hemp flower with tweezers beside microscope and CBD oil flasks"></div>
<h2 class="abs sub-title">SUBSCRIBE TO OUR SITE</h2>
<div class="abs rule" style="left:664px;top:2769px"></div>
<div class="field" style="top:2807px">Name</div>
<div class="field" style="top:2872px">E mail</div>
<div class="field" style="top:2938px">Phone</div>
<div class="btn" style="left:667px;top:3014px;width:396px;height:57px;font-size:21px">SUBSCRIBE</div>

<!-- Trust band -->
<section class="abs band"></section>
<div class="trust" style="left:141px"><div class="dot"><svg width="42" height="28" viewBox="0 0 42 28"><path d="M2 4l14 2 20-2 4 6-4 6-6 6-4 4-4-4-10 0-8-6z" fill="#fff"/></svg></div>MADE IN THE USA</div>
<div class="trust" style="left:491px"><div class="dot"><svg width="40" height="40" viewBox="0 0 40 40"><path d="M20 4l4 14 10-6-6 12 8 2-12 2 2 6-6-4-6 4 2-6-12-2 8-2-6-12 10 6z" fill="#fff"/></svg></div>FULL SPECTRUM CBD</div>
<div class="trust" style="left:863px"><div class="dot"><svg width="34" height="40" viewBox="0 0 34 40"><path d="M12 3h10M14 3v12L4 35h26L20 15V3" fill="none" stroke="#fff" stroke-width="2.5"/><path d="M9 27h16l3 6H6z" fill="#fff"/></svg></div>LAB TESTED</div>

<!-- Footer -->
<footer class="abs footer"></footer>
<div class="abs foot-brand">Qorby Labs</div>
<div class="foot-col" style="left:460px">
  <h4>MENU</h4>
  <ul class="menu-list"><li>HOME</li><li>COMMUNITY</li><li>SHOP</li><li>WHOLESALE</li><li>CONTACT</li></ul>
</div>
<div class="foot-col" style="left:690px">
  <h4>CONTACT US</h4>
  <div class="contact-item"><span class="ico"><svg width="10" height="13" viewBox="0 0 10 13"><path d="M5 0a5 5 0 015 5c0 4-5 8-5 8S0 9 0 5a5 5 0 015-5z" fill="#231f20"/><circle cx="5" cy="5" r="1.8" fill="#fff"/></svg></span><span>2150 Larkspur Avenue<br>Fairview, CA 90000</span></div>
  <div class="contact-item"><span class="ico"><svg width="12" height="12" viewBox="0 0 12 12"><path d="M2 1l3 1-1 3 3 3 3-1 1 3-2 2C5 11 1 7 0 3z" fill="#231f20"/></svg></span><span>Call Us<br>555.010.0148</span></div>
  <div class="contact-item"><span class="ico"><svg width="12" height="9" viewBox="0 0 12 9"><rect width="12" height="9" fill="#231f20"/><path d="M0 0l6 5 6-5" stroke="#fff" fill="none"/></svg></span><span>E mail Us<br>info@qorbylabs.example</span></div>
</div>
<div class="foot-col" style="left:953px">
  <h4>FOLLOW US</h4>
  <div class="contact-item"><span class="ico"></span><span>Like us on<br>FRIENDLINE</span></div>
  <div class="contact-item"><span class="ico"></span><span>Follow us on<br>CHIRPNET</span></div>
  <div class="contact-item"><span class="ico"></span><span>Follow us on<br>WORKLINK</span></div>
</div>
<div class="abs legal">Customer Satisfaction &nbsp;\&nbsp;&nbsp; Shipping &amp; Return Policy &nbsp;\&nbsp;&nbsp; Privacy Policy &nbsp;\&nbsp;&nbsp; Terms of Service</div>
<div class="abs copyright">Copyright © 2020 All Rights Reserved</div>

</body>
</html>
```